Business Card Design Project

Looking to update our business cards. We have a logo with our slogan. We are an IT firm so we wouldlike a modern look.

Industry/Entity Type

Business

```html
<!DOCTYPE html>
<html lang="en">
<head>
<meta charset="utf-8">
<title>Kestrell Business Cards</title>
<link rel="stylesheet" href="https://fonts.googleapis.com/css2?family=Jost:wght@400;500;600&family=Didact+Gothic&display=swap">
<style>
  :root {
    --stage: #8a6040;
    --label: #111111;
    --card-white: #ffffff;
    --card-green: #b1c244;
    --brand-green: #6a8141;
    --ink: #1f1f1f;
    --muted: #3a3a3a;
    --tech-deep: #0e1f6e;
    --tech-mid: #2f5fd0;
    --tech-glow: #e8f2ff;
  }
  * { margin: 0; padding: 0; box-sizing: border-box; }
  html, body { width: 1200px; height: 788px; overflow: hidden; }
  body {
    position: relative;
    background: var(--stage);
    font-family: "Jost", sans-serif;
  }
  .side-label {
    position: absolute;
    width: 525px;
    text-align: center;
    font-family: "Didact Gothic", sans-serif;
    font-size: 21px;
    color: var(--label);
  }
  .card {
    position: absolute;
    width: 525px;
    height: 298px;
    border-radius: 22px;
    overflow: hidden;
  }
  .card--white { background: var(--card-white); }
  .card--green { background: var(--card-green); }
  .card--tech {
    background:
      radial-gradient(ellipse 45% 55% at 52% 52%, var(--tech-glow) 0%, #a9c8f5 30%, transparent 70%),
      linear-gradient(100deg, var(--tech-deep) 0%, var(--tech-mid) 45%, #6d84d8 70%, var(--tech-deep) 100%);
  }
  .brand {
    position: absolute;
    display: flex;
    flex-direction: column;
    align-items: flex-start;
  }
  .brand__row { display: flex; align-items: center; gap: 10px; }
  .brand__dot {
    border-radius: 50%;
    background: var(--brand-green);
    flex: none;
  }
  .brand__name {
    font-weight: 500;
    color: var(--brand-green);
    letter-spacing: 0.06em;
    line-height: 1;
  }
  .brand__tagline {
    font-weight: 600;
    color: var(--ink);
    letter-spacing: 0.22em;
    line-height: 1;
  }
  .brand--small { left: 62px; top: 64px; }
  .brand--small .brand__dot { width: 18px; height: 18px; }
  .brand--small .brand__name { font-size: 36px; }
  .brand--small .brand__tagline { font-size: 10px; margin-top: 7px; }
  .brand--large { left: 106px; top: 112px; }
  .brand--large .brand__dot { width: 26px; height: 26px; }
  .brand--large .brand__name { font-size: 50px; }
  .brand--large .brand__tagline { font-size: 12.5px; margin-top: 9px; letter-spacing: 0.25em; }
  .holder { position: absolute; left: 63px; top: 150px; color: var(--brand-green); }
  .holder__name { font-family: "Didact Gothic", sans-serif; font-size: 17px; }
  .holder__role { font-family: "Didact Gothic", sans-serif; font-size: 13px; margin-top: 3px; }
  .contact {
    position: absolute;
    left: 271px;
    top: 150px;
    list-style: none;
    font-family: "Didact Gothic", sans-serif;
    font-size: 13.5px;
    color: var(--muted);
  }
  .contact li { display: flex; align-items: flex-start; gap: 7px; height: 21.5px; }
  .contact li.contact__address { height: auto; line-height: 18px; }
  .contact svg { width: 12px; height: 12px; margin-top: 3px; flex: none; fill: var(--muted); }
</style>
</head>
<body>
  <p class="side-label" style="left:57px; top:33px;">Front</p>
  <p class="side-label" style="left:634px; top:33px;">Back - 1</p>
  <p class="side-label" style="left:52px; top:404px;">Back - 2</p>
  <p class="side-label" style="left:634px; top:404px;">Back - 3</p>

  <section class="card card--white" style="left:45px; top:80px;">
    <div class="brand brand--small">
      <div class="brand__row"><span class="brand__dot"></span><span class="brand__name">KESTRELL</span></div>
      <span class="brand__tagline">MAKING TECH EFFORTLESS</span>
    </div>
    <div class="holder">
      <p class="holder__name">Your Name</p>
      <p class="holder__role">Designation</p>
    </div>
    <ul class="contact">
      <li><svg viewBox="0 0 12 12"><path d="M2 1h2.5l1 3-1.5 1a7 7 0 0 0 3 3l1-1.5 3 1V11c-5 0-9-4-9-9z"/></svg>+12 345 67890</li>
      <li><svg viewBox="0 0 12 12"><rect x="3" y="1" width="6" height="3"/><rect x="1" y="4.5" width="10" height="5" rx="1"/><rect x="3" y="8" width="6" height="3" fill="#fff"/></svg>+12 345 67890</li>
      <li><svg viewBox="0 0 12 12"><path d="M1 3h10v7H1z M1 3l5 4 5-4" stroke="#3a3a3a" stroke-width="1.2" fill="none"/></svg>info@website.com</li>
      <li><svg viewBox="0 0 12 12"><g fill="none" stroke="#3a3a3a" stroke-width="1"><circle cx="6" cy="6" r="5"/><ellipse cx="6" cy="6" rx="2.2" ry="5"/><path d="M1 6h10"/></g></svg>www.website.com</li>
      <li class="contact__address"><svg viewBox="0 0 12 12"><path d="M6 1l5 5H9.5v5h-2.5V8H5v3H2.5V6H1z"/></svg><span>#0000, Street Name<br>Area Name, Country Code</span></li>
    </ul>
  </section>

  <section class="card card--white" style="left:621px; top:80px;">
    <div class="brand brand--large">
      <div class="brand__row"><span class="brand__dot"></span><span class="brand__name">KESTRELL</span></div>
      <span class="brand__tagline">MAKING TECH EFFORTLESS</span>
    </div>
  </section>

  <section class="card card--green" style="left:49px; top:454px; height:300px;">
    <div class="brand brand--large" style="top:116px;">
      <div class="brand__row"><span class="brand__dot"></span><span class="brand__name">KESTRELL</span></div>
      <span class="brand__tagline">MAKING TECH EFFORTLESS</span>
    </div>
  </section>

  <section class="card card--tech" style="left:621px; top:454px; height:300px;" role="img" aria-label="Abstract blue technology backdrop with glowing light rings, binary digits and a wireframe globe">
    <div class="brand brand--large" style="top:116px;">
      <div class="brand__row"><span class="brand__dot"></span><span class="brand__name">KESTRELL</span></div>
      <span class="brand__tagline">MAKING TECH EFFORTLESS</span>
    </div>
  </section>
</body>
</html>
```